Constructor Company /Carpenter

We need a high quality design for a Brochure up to 8pages.Copmany does plastering, building houses, make renovation of houses.
Updates

Ich brauche zusätzliche Tage um durchzusehen

Target Market(s)

The Brochure is a high quality hand out for architects.

Industry/Entity Type

Construction Company

Font styles to use
Sans Serif

Colors

Designer to choose colors to be used in the design.

Requirements
Must have
• You can build the brochure like the website www.qelvorix.ch is built. The brochure needs to look clean, modern and professionell.
• The brochure need to have the same colors like website www.qelvorix.ch

```html
<!DOCTYPE html>
<html lang="de">
<head>
<meta charset="utf-8">
<title>Qelvorix Bau GmbH – Broschüre</title>
<link href="https://fonts.googleapis.com/css2?family=Montserrat:wght@600;700;800&family=Open+Sans:wght@400;600&display=swap" rel="stylesheet">
<style>
:root{
  --blue:#1f4fa3;
  --blue-dark:#163a7c;
  --ink:#2b2f36;
  --muted:#6b717c;
  --dark-band:#2a2d33;
  --paper:#ffffff;
  --stage:#cfcbc7;
  --photo-a:#b9c2cc;
  --photo-b:#d9d4cc;
  --photo-c:#8fb0c9;
  --photo-d:#a9b29a;
}
*{box-sizing:border-box;margin:0;padding:0}
html,body{width:1200px;height:2400px;overflow:hidden}
body{background:var(--stage);font-family:"Open Sans",Arial,sans-serif;color:var(--ink);position:relative}
.spread{position:absolute;left:80px;width:1040px;height:736px;display:flex;box-shadow:0 10px 30px rgba(0,0,0,.18)}
.spread--cover{top:48px}
.spread--company{top:832px}
.spread--skills{top:1616px}
.page{position:relative;width:520px;height:736px;background:var(--paper);overflow:hidden}
.page--left{border-right:1px solid #e6e6e6}
.photo{position:absolute}
.h-section{font-family:"Montserrat",Arial,sans-serif;font-weight:800;font-size:20px;color:var(--blue);letter-spacing:1px;text-transform:uppercase}
.h-small{font-family:"Montserrat",Arial,sans-serif;font-weight:700;font-size:12px;color:var(--blue);text-transform:uppercase;letter-spacing:.5px}
.copy{font-size:10.5px;line-height:1.55;color:var(--muted)}
.brand{display:flex;align-items:center;gap:8px;font-family:"Montserrat",Arial,sans-serif;font-weight:700;font-size:16px;color:var(--ink)}
.brand-mark{width:14px;height:14px;background:var(--blue)}
.edge{position:absolute;top:0;bottom:0;width:26px;background:var(--blue)}

/* cover back */
.back-intro{position:absolute;left:40px;top:44px;width:440px}
.back-intro .copy{margin-top:10px}
.promise{position:absolute;left:40px;top:236px;width:440px;background:var(--dark-band);padding:16px 18px}
.promise h3{font-family:"Montserrat",Arial,sans-serif;font-size:12px;color:#fff;text-transform:uppercase;margin-bottom:10px}
.promise ul{list-style:none;columns:2;column-gap:18px}
.promise li{font-size:10px;color:#e5e7eb;line-height:1.9;padding-left:12px;position:relative}
.promise li::before{content:"";position:absolute;left:0;top:7px;width:5px;height:5px;background:var(--blue)}
.contact{position:absolute;left:40px;top:520px;list-style:none}
.contact li{display:flex;align-items:center;gap:10px;font-size:11px;color:var(--ink);line-height:2.1}
.contact svg{width:14px;height:14px;fill:var(--blue)}
.back-brand{position:absolute;left:40px;bottom:44px}

/* cover front */
.front-brand{position:absolute;left:40px;top:34px}
.front-title{position:absolute;right:56px;top:560px;text-align:right;font-family:"Montserrat",Arial,sans-serif;font-weight:800;font-size:23px;line-height:1.4;color:var(--blue);text-transform:uppercase;letter-spacing:1px}

/* company */
.team-grid{position:absolute;left:56px;top:150px;width:400px;display:grid;grid-template-columns:1fr 1fr;gap:10px}
.team-grid .tile{height:128px;background:linear-gradient(160deg,var(--photo-b),var(--photo-a))}
.ref-grid{position:absolute;left:40px;top:90px;width:420px;display:grid;grid-template-columns:1fr 1fr;grid-auto-rows:140px;gap:8px}

/* skills */
.skill-photos{position:absolute;left:0;top:60px;width:170px;display:flex;flex-direction:column;gap:8px}
.skill-photos div{height:180px}
.skill-block{position:absolute}
.skill-block ul{list-style:none;margin-top:6px}
.skill-block li{font-size:10px;color:var(--muted);line-height:1.8;padding-left:14px;position:relative}
.skill-block li::before{content:"✓";position:absolute;left:0;color:var(--blue);font-weight:700}
.skill-block.two ul{columns:2;column-gap:18px}
.skill-rule{position:absolute;left:40px;right:40px;height:1px;background:#e2e4e8}
</style>
</head>
<body>

<!-- Spread 1: back and front cover -->
<section class="spread spread--cover">
  <article class="page page--left back-cover">
    <div class="back-intro">
      <h2 class="h-small">Über uns</h2>
      <p class="copy">Als Gipsergeschäft aus Aesch begleiten wir Architekten und Bauherren bei Neubau, Umbau und Renovation. Wir arbeiten sauber, termingerecht und mit hochwertigen Materialien – vom ersten Entwurf bis zur Übergabe.</p>
      <p class="copy">Unser erfahrenes Team legt Wert auf Präzision, offene Kommunikation und zuverlässige Zusammenarbeit auf jeder Baustelle in Basel und Umgebung.</p>
    </div>
    <div class="promise">
      <h3>Was Sie von uns erwarten können</h3>
      <ul>
        <li>Persönliche Beratung</li>
        <li>Saubere Ausführung</li>
        <li>Termintreue</li>
        <li>Faire Offerten</li>
        <li>Erfahrene Fachleute</li>
        <li>Qualität mit Garantie</li>
      </ul>
    </div>
    <div class="photo" role="img" aria-label="Teamfoto von vier Mitarbeitern in weisser Arbeitskleidung" style="left:40px;top:346px;width:440px;height:150px;background:linear-gradient(180deg,#e9eaec,#c7ccd2)"></div>
    <ul class="contact">
      <li><svg viewBox="0 0 24 24"><path d="M6.6 10.8a15.1 15.1 0 006.6 6.6l2.2-2.2c.3-.3.7-.4 1-.2 1.1.4 2.3.6 3.6.6.6 0 1 .4 1 1V20c0 .6-.4 1-1 1C10.6 21 3 13.4 3 4c0-.6.4-1 1-1h3.5c.6 0 1 .4 1 1 0 1.3.2 2.5.6 3.6.1.3 0 .7-.2 1z"/></svg>061 555 01 20</li>
      <li><svg viewBox="0 0 24 24"><path d="M3 5h18v14H3zm2 2v.5l7 4.5 7-4.5V7zm0 2.9V17h14V9.9l-7 4.5z"/></svg>info@qelvorix.ch</li>
      <li><svg viewBox="0 0 24 24"><path d="M12 2a10 10 0 100 20 10 10 0 000-20zm6.9 9h-3a15 15 0 00-1.3-6A8 8 0 0118.9 11zM12 4c.9 1.2 1.8 3.6 2 7h-4c.2-3.4 1.1-5.8 2-7zM9.4 5a15 15 0 00-1.3 6h-3A8 8 0 019.4 5zM5.1 13h3a15 15 0 001.3 6 8 8 0 01-4.3-6zM12 20c-.9-1.2-1.8-3.6-2-7h4c-.2 3.4-1.1 5.8-2 7zm2.6-1a15 15 0 001.3-6h3a8 8 0 01-4.3 6z"/></svg>www.qelvorix.ch</li>
      <li><svg viewBox="0 0 24 24"><path d="M12 2a7 7 0 00-7 7c0 5 7 13 7 13s7-8 7-13a7 7 0 00-7-7zm0 9.5A2.5 2.5 0 1112 6.5a2.5 2.5 0 010 5z"/></svg>Musterweg 12, 4147 Aesch</li>
    </ul>
    <div class="brand back-brand"><span class="brand-mark"></span>Qelvorix Bau GmbH</div>
  </article>

  <article class="page front-cover">
    <svg width="520" height="736" viewBox="0 0 520 736" style="position:absolute;inset:0">
      <polygon points="300,0 520,0 520,90 260,90" fill="var(--blue)"/>
      <polygon points="470,90 520,90 520,500 494,500" fill="var(--blue-dark)"/>
      <polygon points="320,680 520,650 520,736 280,736" fill="var(--blue)"/>
    </svg>
    <div class="brand front-brand"><span class="brand-mark"></span>Qelvorix Bau GmbH</div>
    <div class="photo" role="img" aria-label="Heller Innenraum im Umbau mit frisch verputzten Wänden" style="left:0;top:90px;width:494px;height:410px;background:linear-gradient(135deg,#eef0f2,#c9cdd2 60%,#b8a98f)"></div>
    <h1 class="front-title">Ihr Gipser aus Aesch<br>in Basel und Umgebung</h1>
  </article>
</section>

<!-- Spread 2: company and references -->
<section class="spread spread--company">
  <article class="page page--left">
    <div class="edge" style="left:0"></div>
    <h2 class="h-section" style="position:absolute;left:56px;top:40px">Unternehmen</h2>
    <p class="copy" style="position:absolute;left:56px;top:76px;width:400px">Seit vielen Jahren steht unser Familienbetrieb für solide Handwerksarbeit. Wir verbinden Tradition mit modernen Techniken und realisieren Projekte jeder Grösse.</p>
    <div class="team-grid">
      <div class="tile" role="img" aria-label="Porträt Mitarbeiter"></div>
      <div class="tile" role="img" aria-label="Porträt Mitarbeiter"></div>
      <div class="tile" role="img" aria-label="Porträt Mitarbeiter"></div>
      <div class="tile" role="img" aria-label="Porträt Mitarbeiter"></div>
    </div>
    <p class="copy" style="position:absolute;left:56px;top:440px;width:400px">Unser Team aus gelernten Gipsern und Bauleuten arbeitet eng mit Architekten zusammen. Kurze Wege, klare Absprachen und ein verlässlicher Ansprechpartner sorgen für einen reibungslosen Ablauf.</p>
    <p class="copy" style="position:absolute;left:56px;top:530px;width:400px">Wir übernehmen Verantwortung für jedes Detail und stehen auch nach Abschluss der Arbeiten gerne für Sie da.</p>
  </article>
  <article class="page">
    <div class="edge" style="right:0"></div>
    <h2 class="h-section" style="position:absolute;left:40px;top:40px">Referenzen</h2>
    <div class="ref-grid">
      <div role="img" aria-label="Mehrfamilienhaus mit neuer Fassade" style="background:linear-gradient(160deg,#dfe3e8,var(--photo-a))"></div>
      <div role="img" aria-label="Holzfassade eines Einfamilienhauses" style="background:linear-gradient(160deg,#c9a982,#8c6c4b)"></div>
      <div role="img" aria-label="Garten mit blauem Schwimmbad" style="background:linear-gradient(160deg,var(--photo-c),#3f86c4)"></div>
      <div role="img" aria-label="Heller Raum mit neuer Decke" style="background:linear-gradient(160deg,#f0efec,#cfc9bf)"></div>
      <div role="img" aria-label="Verputzte Aussenwand mit Treppe" style="background:linear-gradient(160deg,var(--photo-b),#a7a197)"></div>
      <div role="img" aria-label="Renovierter Innenraum" style="background:linear-gradient(160deg,#e4e4e2,#b0b3b7)"></div>
      <div role="img" aria-label="Modernes Haus mit Balkon" style="background:linear-gradient(160deg,#d8dde2,#9aa4ae)"></div>
      <div role="img" aria-label="Terrasse nach Umbau" style="background:linear-gradient(160deg,#cfd6c6,var(--photo-d))"></div>
    </div>
  </article>
</section>

<!-- Spread 3: skills -->
<section class="spread spread--skills">
  <article class="page page--left">
    <div class="skill-photos">
      <div role="img" aria-label="Aussenanlage mit Pflanzen" style="background:linear-gradient(160deg,#b6c59a,#6f8454)"></div>
      <div role="img" aria-label="Gipser beim Verputzen einer Wand" style="background:linear-gradient(160deg,#d6d2cb,#9f988d)"></div>
      <div role="img" aria-label="Fertig renovierter Wohnraum" style="background:linear-gradient(160deg,#ece9e3,#c4bba9)"></div>
    </div>
    <h2 class="h-section" style="position:absolute;left:196px;top:40px">Kompetenzen</h2>
    <div class="skill-block" style="left:196px;top:90px;width:290px">
      <h3 class="h-small">Gipserarbeiten</h3>
      <ul><li>Innenputze und Grundputze</li><li>Abrieb und Glattputz</li><li>Stuckaturen und Profile</li></ul>
    </div>
    <div class="skill-block" style="left:196px;top:220px;width:290px">
      <h3 class="h-small">Neubau</h3>
      <ul><li>Rohbau und Mauerwerk</li><li>Koordination mit Architekten</li><li>Termingerechte Übergabe</li></ul>
    </div>
    <div class="skill-block" style="left:196px;top:350px;width:290px">
      <h3 class="h-small">Umbau &amp; Renovation</h3>
      <ul><li>Altbausanierung</li><li>Wand- und Deckenrenovation</li><li>Risssanierung</li></ul>
    </div>
    <div class="skill-block" style="left:196px;top:480px;width:290px">
      <h3 class="h-small">Trockenbau</h3>
      <ul><li>Leichtbauwände</li><li>Abgehängte Decken</li><li>Vorsatzschalen</li></ul>
    </div>
  </article>
  <article class="page">
    <div class="skill-block two" style="left:40px;top:50px;width:440px">
      <h3 class="h-small">Fassaden</h3>
      <ul><li>Aussenwärmedämmung</li><li>Fassadenputze</li><li>Farbgestaltung</li><li>Sanierung</li></ul>
    </div>
    <div class="skill-rule" style="top:150px"></div>
    <div class="skill-block two" style="left:40px;top:170px;width:440px">
      <h3 class="h-small">Malerarbeiten</h3>
      <ul><li>Innenanstriche</li><li>Lasuren</li><li>Tapezieren</li><li>Lackierarbeiten</li></ul>
    </div>
    <div class="skill-rule" style="top:270px"></div>
    <div class="skill-block two" style="left:40px;top:290px;width:440px">
      <h3 class="h-small">Isolationen</h3>
      <ul><li>Wärmedämmung</li><li>Schallschutz</li><li>Brandschutz</li><li>Estrichdämmung</li></ul>
    </div>
    <div class="skill-rule" style="top:390px"></div>
    <div class="skill-block two" style="left:40px;top:410px;width:440px">
      <h3 class="h-small">Dienstleistungen</h3>
      <ul><li>Beratung vor Ort</li><li>Offertstellung</li><li>Bauleitung</li><li>Reparaturen</li></ul>
    </div>
    <div class="skill-rule" style="top:510px"></div>
    <div class="skill-block two" style="left:40px;top:530px;width:440px">
      <h3 class="h-small">Kontakt</h3>
      <ul><li>061 555 01 20</li><li>info@qelvorix.ch</li><li>www.qelvorix.ch</li><li>4147 Aesch</li></ul>
    </div>
  </article>
</section>

</body>
</html>
```